Front & Back cover design for timber flooring brochure - A4 size

I need a design for the front and back cover of an A4 sized brochure for a timber and concrete flooring company called "Kestrel Row Floors". The front cover should include the logo (attached), and an image + tagline for each of the three products/services that they offer which are:

1. Timber Flooring
2. Concrete Grinding & Sealing
3. Floor sanding (i have attached a photo for each of these three - however feel free to use other images if you feel they are better).

The back cover should be simple, perhaps just a continuation of the colour or graphic scheme on the front with the company contact details at the bottom.

Industry/Entity Type

Flooring

Requirements
Must have
• front cover has to have the logo with an image and text of the 3 services described. You can use the images attached or your own.

```html
<!DOCTYPE html>
<html lang="en">
<head>
<meta charset="utf-8">
<title>Kestrel Row Floors – Brochure Cover</title>
<link rel="stylesheet" href="https://fonts.googleapis.com/css2?family=Cinzel:wght@400;600;700&display=swap">
<style>
  :root {
    --bg-top: #0a0b0b;
    --bg-upper: #232925;
    --bg-mid: #5c6857;
    --bg-low: #9ea29b;
    --bg-bottom: #ffffff;
    --brand-brown: #8a4a16;
    --brand-tile: #e08a2a;
    --service-gold: #d9a52c;
    --frame-white: #f4f2ee;
    --timber-warm: #a8471c;
    --concrete-green: #a9b488;
  }
  * { box-sizing: border-box; margin: 0; padding: 0; }
  html, body { width: 844px; height: 1200px; overflow: hidden; }
  body { background: #ffffff; }
  .cover {
    position: relative;
    width: 844px;
    height: 1200px;
    overflow: hidden;
    background: linear-gradient(180deg,
      var(--bg-top) 0%,
      var(--bg-upper) 22%,
      var(--bg-mid) 48%,
      var(--bg-low) 68%,
      #e9eae8 86%,
      var(--bg-bottom) 100%);
    font-family: "Cinzel", "Times New Roman", serif;
  }
  .brand {
    position: absolute;
    top: 92px;
    left: 0;
    width: 844px;
    display: flex;
    justify-content: center;
    align-items: center;
    gap: 22px;
  }
  .brand-square {
    width: 52px;
    height: 52px;
    background: var(--brand-tile);
  }
  .brand-name {
    color: var(--brand-brown);
    font-weight: 700;
    font-size: 50px;
    letter-spacing: 3px;
    line-height: 1;
  }
  .services {
    position: absolute;
    top: 262px;
    left: 60px;
    width: 730px;
    display: flex;
    justify-content: space-between;
    align-items: flex-start;
    list-style: none;
    color: var(--service-gold);
    font-size: 16.5px;
    letter-spacing: 1px;
    text-align: center;
  }
  .services li { line-height: 21px; }
  .services .dot {
    width: 9px; height: 9px; border-radius: 50%;
    background: var(--service-gold);
    margin-top: 7px;
  }
  .services .first { margin-top: 12px; }
  .services .second { margin-top: 12px; }
  .photo {
    position: absolute;
  }
  .photo-timber {
    left: 74px; top: 596px; width: 142px; height: 227px;
    background: linear-gradient(160deg, #c9602a 0%, var(--timber-warm) 45%, #6e2a0f 100%);
  }
  .photo-concrete {
    left: 626px; top: 596px; width: 152px; height: 218px;
    background: radial-gradient(circle at 45% 35%, #e6ecd6 0%, var(--concrete-green) 35%, #7f8e5a 100%);
  }
  .reflection {
    position: absolute;
    opacity: 0.35;
  }
  .reflection-timber {
    left: 74px; top: 823px; width: 142px; height: 90px;
    background: linear-gradient(180deg, #7e3a1a 0%, rgba(255,255,255,0) 100%);
  }
  .reflection-concrete {
    left: 626px; top: 814px; width: 152px; height: 90px;
    background: linear-gradient(180deg, #8c9a6c 0%, rgba(255,255,255,0) 100%);
  }
  .swatch-grid {
    position: absolute;
    left: 215px; top: 478px;
    width: 412px; height: 482px;
    padding: 4px;
    background: var(--frame-white);
    display: grid;
    grid-template-columns: repeat(5, 1fr);
    grid-template-rows: repeat(6, 1fr);
    gap: 4px;
  }
  .swatch-grid span { display: block; }
  .swatch-reflection {
    position: absolute;
    left: 215px; top: 960px;
    width: 412px; height: 130px;
    background: linear-gradient(180deg, rgba(150,110,70,0.45) 0%, rgba(255,255,255,0) 100%);
  }
</style>
</head>
<body>
  <main class="cover">
    <header class="brand">
      <span class="brand-name">Kestrel Row</span>
      <span class="brand-square"></span>
      <span class="brand-name">Floors</span>
    </header>

    <ul class="services">
      <li class="first">Floor Sanding</li>
      <li class="dot" aria-hidden="true"></li>
      <li class="second">Timber Flooring</li>
      <li class="dot" aria-hidden="true"></li>
      <li>Concrete&nbsp; Grinding<br>&amp; Sealing</li>
    </ul>

    <div class="photo photo-timber" role="img" aria-label="Close-up of a glossy sanded red timber floor"></div>
    <div class="reflection reflection-timber" aria-hidden="true"></div>

    <div class="photo photo-concrete" role="img" aria-label="Polished and sealed green-grey concrete floor with light reflections"></div>
    <div class="reflection reflection-concrete" aria-hidden="true"></div>

    <div class="swatch-grid" role="img" aria-label="Grid of thirty timber flooring sample tiles in various wood species and tones">
      <span style="background:#8a4a1e"></span>
      <span style="background:#6a3219"></span>
      <span style="background:#5e2a14"></span>
      <span style="background:#7a3e1c"></span>
      <span style="background:#9a5a1e"></span>

      <span style="background:#6e3a1a"></span>
      <span style="background:#d2ae84"></span>
      <span style="background:#e0a47e"></span>
      <span style="background:#5a2314"></span>
      <span style="background:#6a331e"></span>

      <span style="background:#a8661e"></span>
      <span style="background:#9a5c1a"></span>
      <span style="background:#8e5216"></span>
      <span style="background:#c4845c"></span>
      <span style="background:#e4c49a"></span>

      <span style="background:#b8763a"></span>
      <span style="background:#5a2416"></span>
      <span style="background:#6a3a22"></span>
      <span style="background:#5a2e1c"></span>
      <span style="background:#9c5e1e"></span>

      <span style="background:#3e1a10"></span>
      <span style="background:#8e3e1a"></span>
      <span style="background:#a8641c"></span>
      <span style="background:#c48a3a"></span>
      <span style="background:#d4b694"></span>

      <span style="background:#4a1e12"></span>
      <span style="background:#5e3620"></span>
      <span style="background:#a87a52"></span>
      <span style="background:#7a3e1e"></span>
      <span style="background:#5a2616"></span>
    </div>
    <div class="swatch-reflection" aria-hidden="true"></div>
  </main>
</body>
</html>
```